HVL Regal Business Card Design 2020

Harbor Vale Living is looking for a business card that is clean and straight to the point but still looks high-end and attractive. We are a team comprised of management and field professionals focused on the high-end residential marketplace. We serve homeowners and trade professionals directly based out of the Metrowest/Boston area. We provide client services as well as construction/renovation services.
We are aiming for a black and white feel (white background and black text) and a matte finish with rounded edges.

We want to emphasis our vision of "Properties - Projects - Partners".
Dana Pritchell is the president of HVL

Please include the following areas we service: Boston/Cape/Newport
Please make sure to include Dana's mobile (617) 555 0143 & office number (617) 555 0187, email dana@harborvaleliving.example and website www.harborvaleliving.example

Colors

Designer to choose only greyscale colors for use in the design.

Requirements
Must have
• Include "Properties - Projects - Partners" in design

Include "After Hours Emergency Support # 1800 555 0199" with icon

```html
<!DOCTYPE html>
<html lang="en">
<head>
<meta charset="utf-8">
<title>Harbor Vale Living – Business Card</title>
<link href="https://fonts.googleapis.com/css2?family=Montserrat:wght@600;700&family=Lato:wght@400;700&display=swap" rel="stylesheet">
<style>
  :root {
    --ink: #262626;
    --ink-soft: #555555;
    --grey: #7a7a7a;
    --faint: #ececec;
    --paper: #ffffff;
  }
  * { margin: 0; padding: 0; box-sizing: border-box; }
  html, body { width: 1038px; height: 1200px; overflow: hidden; background: var(--paper); }
  .canvas { position: relative; width: 1038px; height: 1200px; }

  .back-panel {
    position: absolute; left: 124px; top: 100px; width: 284px; height: 451px;
    background: var(--ink); color: var(--paper);
  }
  .back-panel .brand-name {
    position: absolute; left: 0; right: 0; top: 40px; text-align: center;
    font-family: 'Montserrat', sans-serif; font-weight: 700; font-size: 82px;
    line-height: 1; letter-spacing: -2px;
  }
  .back-panel .brand-tagline {
    position: absolute; left: 0; right: 0; top: 145px; text-align: center;
    font-family: 'Montserrat', sans-serif; font-weight: 700; font-size: 13.5px;
    letter-spacing: 1.5px;
  }
  .pillars { position: absolute; left: 52px; top: 205px; list-style: none; }
  .pillars li {
    display: flex; align-items: center; height: 64px;
    font-family: 'Lato', sans-serif; font-weight: 700; font-size: 24px;
  }
  .pillars svg { width: 42px; height: 40px; margin-right: 17px; flex: none; }

  .divider { position: absolute; left: 423px; top: 100px; width: 6px; height: 451px; background: var(--ink); }

  .front-decor { position: absolute; left: 742px; top: 100px; width: 172px; height: 451px; background: var(--faint); }

  .person { position: absolute; left: 500px; top: 160px; }
  .person .name {
    font-family: 'Montserrat', sans-serif; font-weight: 700; font-size: 39px;
    color: var(--ink); line-height: 1; letter-spacing: 0.3px;
  }
  .person .title {
    margin-top: 14px; font-family: 'Montserrat', sans-serif; font-weight: 600;
    font-size: 24px; color: var(--ink-soft);
  }
  .contacts { position: absolute; left: 503px; top: 275px; list-style: none; }
  .contacts li {
    display: flex; align-items: center; height: 52.7px;
    font-family: 'Lato', sans-serif; font-size: 18px; color: var(--ink-soft);
  }
  .contacts .icon {
    width: 36px; height: 36px; border-radius: 50%; background: var(--ink);
    display: flex; align-items: center; justify-content: center; margin-right: 16px;
  }
  .contacts .icon svg { width: 18px; height: 18px; }

  .brand-lockup { position: absolute; left: 0; right: 0; top: 712px; text-align: center; color: var(--ink); }
  .brand-lockup .brand-name {
    font-family: 'Montserrat', sans-serif; font-weight: 700; font-size: 200px;
    line-height: 1; letter-spacing: -6px;
  }
  .brand-lockup .brand-tagline {
    margin-top: 12px; font-family: 'Montserrat', sans-serif; font-weight: 600;
    font-size: 27px; letter-spacing: 3px; word-spacing: 8px;
  }

  .service-areas {
    position: absolute; left: 0; right: 0; top: 1026px; display: flex; justify-content: center;
    list-style: none; font-family: 'Lato', sans-serif; font-weight: 700; font-size: 24px; color: var(--grey);
  }
  .service-areas li { display: flex; align-items: center; margin: 0 12px; }
  .service-areas li::before {
    content: ""; width: 11px; height: 11px; border-radius: 50%; background: var(--grey);
    margin-right: 14px; margin-top: 4px;
  }
</style>
</head>
<body>
<main class="canvas">

  <section class="back-panel">
    <div class="brand-name">HVL</div>
    <div class="brand-tagline">HARBOR VALE LIVING</div>
    <ul class="pillars">
      <li>
        <svg viewBox="0 0 42 40" fill="none" stroke="#fff" stroke-width="2">
          <rect x="9" y="2" width="22" height="35"/>
          <g fill="#fff" stroke="none">
            <rect x="13" y="6" width="3" height="3"/><rect x="18.5" y="6" width="3" height="3"/><rect x="24" y="6" width="3" height="3"/>
            <rect x="13" y="12" width="3" height="3"/><rect x="18.5" y="12" width="3" height="3"/><rect x="24" y="12" width="3" height="3"/>
            <rect x="13" y="18" width="3" height="3"/><rect x="18.5" y="18" width="3" height="3"/><rect x="24" y="18" width="3" height="3"/>
            <rect x="13" y="24" width="3" height="3"/><rect x="18.5" y="24" width="3" height="3"/><rect x="24" y="24" width="3" height="3"/>
            <rect x="17" y="30" width="6" height="7"/>
          </g>
        </svg>
        Properties
      </li>
      <li>
        <svg viewBox="0 0 42 40" fill="none" stroke="#fff" stroke-width="2" stroke-linejoin="round">
          <path d="M3 14 L11 6 H21 V28 H3 Z M3 14 H11 V6"/>
          <path d="M17 16 L24 9 H37 V37 H17 Z M17 16 H24 V9"/>
        </svg>
        Projects
      </li>
      <li>
        <svg viewBox="0 0 42 40" fill="#fff">
          <circle cx="8" cy="9" r="5"/><circle cx="34" cy="9" r="5"/><circle cx="21" cy="13" r="6.5"/>
          <path d="M0 26 Q0 17 8 17 Q13 17 14 20 L14 26 Z"/>
          <path d="M42 26 Q42 17 34 17 Q29 17 28 20 L28 26 Z"/>
          <path d="M9 38 Q9 22 21 22 Q33 22 33 38 Z"/>
        </svg>
        Partners
      </li>
    </ul>
  </section>

  <div class="divider"></div>

  <section class="card-front">
    <div class="front-decor"></div>
    <div class="person">
      <div class="name">DANA PRITCHELL</div>
      <div class="title">President</div>
    </div>
    <ul class="contacts">
      <li>
        <span class="icon"><svg viewBox="0 0 18 18" fill="none" stroke="#fff" stroke-width="1.6"><rect x="5" y="1.5" width="8" height="15" rx="1.2"/><circle cx="9" cy="13.8" r="0.8" fill="#fff"/></svg></span>
        (617) 555 0143
      </li>
      <li>
        <span class="icon"><svg viewBox="0 0 18 18" fill="#fff"><path d="M4.5 2 L7 5.5 L5.6 7.2 Q7.2 10.6 10.8 12.4 L12.5 11 L16 13.5 L14.3 16 Q8.5 16 4.8 11.8 Q1.8 8 2 3.7 Z"/></svg></span>
        (617) 555 0187
      </li>
      <li>
        <span class="icon"><svg viewBox="0 0 18 18" fill="#fff"><path d="M2 4.5 H16 V6 L9 10.2 L2 6 Z"/><path d="M2 7.6 L9 11.8 L16 7.6 V14 H2 Z"/></svg></span>
        dana@harborvaleliving.example
      </li>
      <li>
        <span class="icon"><svg viewBox="0 0 18 18" fill="none" stroke="#fff" stroke-width="1.5"><circle cx="9" cy="9" r="7"/><path d="M2 9 H16 M9 2 Q5 9 9 16 M9 2 Q13 9 9 16"/></svg></span>
        www.harborvaleliving.example
      </li>
    </ul>
  </section>

  <section class="brand-lockup">
    <div class="brand-name">HVL</div>
    <div class="brand-tagline">HARBOR VALE LIVING</div>
  </section>

  <ul class="service-areas">
    <li>Boston</li>
    <li>Metrowest</li>
    <li>South Shore</li>
    <li>Cape</li>
    <li>Newport</li>
  </ul>

</main>
</body>
</html>
```